Cd Cover design for Chicago based record label.

Cd Cover design for a new single! Song is dedicated to exotic dancers. We do not want our artist pictures on this one. So please use your imagination. Song Title: "Slow Burnout". Thanks? Artist: Lenny Sparrows feat. Kid Tango.

```html
<!DOCTYPE html>
<html lang="en">
<head>
<meta charset="utf-8">
<title>Slow Burnout — Single Cover</title>
<link rel="stylesheet" href="https://fonts.googleapis.com/css2?family=Orbitron:wght@500&display=swap">
<style>
  :root {
    --teal: #1596a3;
    --teal-deep: #0f8794;
    --signal-red: #ff1208;
    --neon-red: #ff2a10;
    --neon-glow: rgba(255, 40, 20, 0.55);
  }
  html, body {
    margin: 0;
    padding: 0;
    width: 1200px;
    height: 1200px;
    overflow: hidden;
    background: var(--teal);
  }
  .cover {
    position: relative;
    width: 1200px;
    height: 1200px;
    overflow: hidden;
    background:
      radial-gradient(ellipse at 30% 40%, rgba(255,255,255,0.06), transparent 60%),
      var(--teal);
  }
  .cover__art {
    position: absolute;
    inset: 0;
    width: 1200px;
    height: 1200px;
  }
  .cover__title-haze {
    position: absolute;
    left: 60px;
    top: 78px;
    width: 750px;
    height: 96px;
    border-radius: 30px;
    background: rgba(210, 40, 30, 0.35);
    filter: blur(18px);
  }
  .cover__title {
    position: absolute;
    left: 76px;
    top: 80px;
    margin: 0;
    font-family: "Orbitron", sans-serif;
    font-weight: 500;
    font-size: 64px;
    line-height: 84px;
    letter-spacing: 4px;
    text-transform: uppercase;
    white-space: nowrap;
    color: transparent;
    -webkit-text-stroke: 2.5px var(--neon-red);
    text-shadow:
      0 0 6px var(--neon-glow),
      0 0 16px var(--neon-glow);
  }
</style>
</head>
<body>
  <main class="cover">
    <svg class="cover__art" viewBox="0 0 1200 1200" xmlns="http://www.w3.org/2000/svg">
      <defs>
        <clipPath id="spotlight-clip">
          <circle cx="800" cy="758" r="426"/>
        </clipPath>
        <radialGradient id="dancer-tone" cx="50%" cy="50%" r="50%">
          <stop offset="0%" stop-color="#1596a3" stop-opacity="0.85"/>
          <stop offset="70%" stop-color="#1596a3" stop-opacity="0.45"/>
          <stop offset="100%" stop-color="#1596a3" stop-opacity="0"/>
        </radialGradient>
      </defs>

      <rect class="pole" x="962" y="0" width="16" height="1200" fill="var(--signal-red)"/>

      <circle class="spotlight-disc" cx="800" cy="758" r="426" fill="var(--signal-red)"/>

      <g clip-path="url(#spotlight-clip)">
        <rect class="pole pole--inside-disc" x="962" y="0" width="16" height="1200" fill="var(--teal)"/>
      </g>

      <ellipse class="dancer-silhouette" role="img"
               aria-label="Teal silhouette of a dancer arching backwards on the pole"
               cx="910" cy="820" rx="230" ry="380"
               fill="url(#dancer-tone)"/>
    </svg>

    <div class="cover__title-haze" aria-hidden="true"></div>
    <h1 class="cover__title">Slow Burnout</h1>
  </main>
</body>
</html>
```